Dynamic Templates

Our company hosts web stores for our clients. They can set up as many as they wish on our platform, and select from the stock templates we provide. We are looking to increase the number of available stock templates.

Because our users can dynamically control many of the template elements - specifically colors - they have to be flexible and abide by certain rules. These rules are spelled out in the attached documents.

Here are links to two of our most used templates:
http://fernridge.vexalcart.example/
http://stampled.vexalcart.example/

Templates need to have a landing page (what you see when first clicking one of the above links). There also needs to be a category page (what you see when clicking any category) and a product detail page (what you see when you arrive at an individual product, where there are various cart options like Buy Now or Request Info).

```html
<!DOCTYPE html>
<html lang="en">
<head>
<meta charset="utf-8">
<title>VexalCart – Distributor Website Solutions</title>
<link rel="stylesheet" href="https://fonts.googleapis.com/css2?family=Noto+Serif:ital,wght@0,400;0,700;1,400&family=Open+Sans:ital,wght@0,400;1,400;1,600&display=swap">
<style>
  :root {
    --page-bg: #ffffff;
    --band: #8ac7c5;
    --footer-bg: #f4f4f4;
    --footer-edge: #e6e6e6;
    --text: #333333;
    --link: #5e5e5e;
    --heading: #333333;
    --accent: #f7931e;
    --card: #ffffff;
    --tab-bg: #ececec;
    --rule: #c8c8c8;
    --button-top: #8fe01a;
    --button-bottom: #5fb800;
    --button-border: #57a800;
  }
  * { box-sizing: border-box; margin: 0; padding: 0; }
  html, body {
    width: 1160px; height: 1200px; overflow: hidden;
    background: var(--page-bg);
    font-family: "Noto Serif", Georgia, serif;
    color: var(--text);
  }
  .page { position: relative; width: 1160px; height: 1200px; }

  /* Header */
  .brand { position: absolute; left: 101px; top: 42px; display: flex; align-items: center; gap: 8px; }
  .brand-dot { width: 37px; height: 37px; border-radius: 50%; background: var(--accent); }
  .brand-name { font-family: "Open Sans", Arial, sans-serif; font-size: 19px; color: var(--accent); line-height: 1; }
  .contact-top { position: absolute; right: 123px; top: 40px; text-align: right; font-family: "Open Sans", Arial, sans-serif; }
  .contact-top .phone { font-size: 22px; font-style: italic; font-weight: 600; letter-spacing: 2px; color: #444; }
  .contact-top .phone small { font-size: 13px; font-weight: 400; color: #888; letter-spacing: 1px; margin-right: 3px; }
  .contact-top .email { font-size: 13px; letter-spacing: 1.2px; color: #333; margin-top: -2px; }

  /* Showcase band */
  .showcase {
    position: absolute; left: 0; top: 114px; width: 1160px; height: 284px;
    background: var(--band);
  }
  .showcase-shadow { position: absolute; left: 0; top: 398px; width: 1160px; height: 30px; background: linear-gradient(#eeeeee, rgba(255,255,255,0)); }

  .product-card {
    position: absolute; top: 21px; width: 230px; height: 240px;
    background: var(--card); border-radius: 6px;
    box-shadow: 0 1px 4px rgba(0,0,0,0.18);
    padding: 12px;
  }
  .product-photo { width: 100%; height: 100%; border-radius: 4px; }
  .photo-pad { background: radial-gradient(circle at 50% 50%, #c9505a, #f6e3e4 85%); }
  .photo-mug { background: radial-gradient(circle at 50% 50%, #4a5d88, #e7eaf1 85%); }
  .photo-bag { background: radial-gradient(circle at 50% 50%, #dcdcdc, #f8f8f8 85%); }
  .photo-bank { background: radial-gradient(circle at 50% 50%, #8b6b5e, #f1e9e5 85%); }

  /* Intro */
  .intro { position: absolute; left: 100px; top: 440px; width: 680px; }
  .intro h1 { font-weight: 400; font-size: 34px; line-height: 34px; color: var(--heading); }
  .intro h2 { font-weight: 400; font-size: 28px; line-height: 34px; color: var(--heading); margin: 26px 0 22px -2px; }
  .intro p { font-size: 13px; line-height: 20px; color: #222; }
  .intro .lead { width: 630px; margin-top: 13px; }

  .cta {
    position: absolute; left: 820px; top: 443px; width: 230px; height: 45px;
    border-radius: 5px; border: 1px solid var(--button-border);
    background: linear-gradient(var(--button-top), var(--button-bottom));
    box-shadow: 0 1px 3px rgba(0,0,0,0.2);
    color: #fff; font-style: italic; font-size: 23px; text-align: center; line-height: 42px;
    text-decoration: none;
  }

  /* Footer */
  .site-footer {
    position: absolute; left: 0; top: 798px; width: 1160px; height: 402px;
    background: var(--footer-bg);
    border-top: 1px solid var(--footer-edge);
  }
  .tab {
    position: absolute; height: 35px; border-radius: 6px; background: var(--tab-bg);
    font-size: 16px; color: #888; line-height: 35px; padding-left: 11px;
  }
  .link-list { position: absolute; list-style: none; font-size: 12px; color: var(--link); }
  .link-list li { height: 18px; line-height: 18px; white-space: nowrap; }
  .link-list li::before { content: "→"; font-family: Arial, sans-serif; font-size: 9px; color: #999; margin-right: 5px; }
  .divider { position: absolute; top: 37px; width: 1px; height: 252px; background: var(--rule); }
  .search-field {
    position: absolute; left: 820px; top: 92px; width: 165px; height: 26px;
    border: 1px solid #cfcfcf; border-radius: 13px; background: #fff;
    box-shadow: inset 0 1px 2px rgba(0,0,0,0.12);
  }
  .search-field svg { position: absolute; right: 9px; top: 6px; }
  .go-button {
    position: absolute; left: 993px; top: 91px; width: 44px; height: 28px;
    border: 1px solid #bbb; border-radius: 14px; background: linear-gradient(#fafafa, #e0e0e0);
    font-style: italic; font-weight: 700; font-size: 14px; color: #666; text-align: center; line-height: 26px;
  }
  .footer-contact { position: absolute; left: 820px; top: 196px; font-size: 12px; line-height: 18px; color: #444; }
  .copyright { position: absolute; left: 100px; top: 330px; font-size: 12px; color: #444; }
</style>
</head>
<body>
<div class="page">
  <header>
    <div class="brand">
      <span class="brand-dot"></span>
      <span class="brand-name">VexalCart</span>
    </div>
    <div class="contact-top">
      <div class="phone"><small>(415)</small>555-0187</div>
      <div class="email">info@vexalcart.example</div>
    </div>
  </header>

  <section class="showcase">
    <div class="product-card" style="left:100px"><div class="product-photo photo-pad" role="img" aria-label="Photo of a red gel wrist-rest mouse pad"></div></div>
    <div class="product-card" style="left:340px"><div class="product-photo photo-mug" role="img" aria-label="Photo of a black mug with a blue grip sleeve"></div></div>
    <div class="product-card" style="left:580px"><div class="product-photo photo-bag" role="img" aria-label="Photo of a clear travel pouch with bottles"></div></div>
    <div class="product-card" style="left:820px"><div class="product-photo photo-bank" role="img" aria-label="Photo of a brown toy coin bank"></div></div>
  </section>
  <div class="showcase-shadow"></div>

  <main class="intro">
    <h1>Welcome To The Future<br>of Promotional Products!</h1>
    <p class="lead">Gone are the days of searching through dog-eared catalogs or trying to make sense of complicated product websites. We do the work for you! We've taken only the very best and most current products and placed them in easy-to-use categories designed for your needs. Take a look at our selection - quality products at excellent prices.</p>
    <h2>Enjoy This Amazing New Resource</h2>
    <p>We know you don't have time to waste; so we've cut to the chase and made it simple! But keep in mind, we do have access to over a million products - so if you don't see what you're looking for or have a special theme or request, let us know - we'll find it!</p>
  </main>
  <a class="cta" href="#">Start Shopping »</a>

  <footer class="site-footer">
    <div class="tab" style="left:100px;top:37px;width:165px">Shop By Category</div>
    <ul class="link-list" style="left:100px;top:88px">
      <li>Apparel</li><li>Auto</li><li>Awards &amp; Recognition</li><li>Bags &amp; Totes</li><li>Business Supplies</li><li>Calendars, Books &amp; Cards</li><li>Caps &amp; Hats</li><li>Clocks &amp; Watches</li><li>Company Outings</li><li>Computer</li><li>Corporate Gifts</li>
    </ul>
    <ul class="link-list" style="left:270px;top:88px">
      <li>Desktop &amp; Office</li><li>Eco Friendly</li><li>Electronics</li><li>Executive Gifts</li><li>Food, Candy &amp; Drink</li><li>Games &amp; Novelties</li><li>Gift Sets</li><li>Golf, Sports &amp; Outdoors</li><li>Healthcare &amp; Safety</li><li>Holiday</li><li>Home &amp; Housewares</li>
    </ul>
    <ul class="link-list" style="left:425px;top:88px">
      <li>Keychains</li><li>Mugs &amp; Drinkware</li><li>Notebooks &amp; Folios</li><li>Pocket &amp; Purse</li><li>Stress Balls &amp; Relievers</li><li>Tools &amp; Hardware</li><li>Tradeshows &amp; Events</li><li>Travel &amp; Luggage</li><li>Writing Instrument</li>
    </ul>
    <div class="divider" style="left:580px"></div>
    <div class="tab" style="left:600px;top:37px;width:165px">Shop By Price</div>
    <ul class="link-list" style="left:602px;top:88px">
      <li>Under $5</li><li>$5 - $10</li><li>$10 - $20</li><li>$20 - $50</li><li>$50 - $100</li><li>$100 - $200</li><li>Over $200</li>
    </ul>
    <div class="divider" style="left:794px"></div>
    <div class="tab" style="left:820px;top:37px;width:165px">Quick Search</div>
    <div class="search-field">
      <svg width="12" height="12" viewBox="0 0 12 12" aria-hidden="true"><circle cx="4.5" cy="4.5" r="3.3" fill="none" stroke="#888" stroke-width="1.4"/><line x1="7" y1="7" x2="11" y2="11" stroke="#888" stroke-width="1.8"/></svg>
    </div>
    <div class="go-button">Go</div>
    <div class="tab" style="left:820px;top:147px;width:109px">Contact Us</div>
    <div class="footer-contact">info@vexalcart.example<br>www.vexalcart.example</div>
    <div class="copyright">© 2010 . VexalCart.example V3 . All Rights Reserved.</div>
  </footer>
</div>
</body>
</html>
```